Business Card for Toffee Parlour

I have a logo for my candy buffet business, and need a business card designed using that logo. Toffee Parlour designs and builds beautiful and delicious candy and dessert tables for all kinds of events. The card should be simple, modern, graphic, colorful, and use the Toffee Parlour Logo.

Target Market(s)

The target market is people hosting major parties and events. This includes brides getting married, parents hosting birthday parties/Sweet Sixteen/Bar Mitzvah/quinceanera parties, and companies hosting corporate events.

Industry/Entity Type

Business

Requirements
Must have
• The business card must have the logo, with or without the tag line.

The following information must be on the card:

Renata Hollis
CEO & Candy Stylist
415.372.6091
renata@toffeeparlourco.example
Nice to have
• I like the idea of having multiple colors of the same design so that several people receiving cards will each receive a different color. Perhaps 3-5 colors or variations on a basic card design.

```html
<!DOCTYPE html>
<html lang="en">
<head>
<meta charset="utf-8">
<title>Toffee Parlour — Business Card</title>
<link rel="stylesheet" href="https://fonts.googleapis.com/css2?family=Didact+Gothic&family=Open+Sans:wght@400;600&family=Poiret+One&display=swap">
<style>
  :root {
    --backdrop: #ecebe8;
    --card: #ffffff;
    --green: #4cb857;
    --pink: #ec1e86;
    --ink: #1e1e1e;
    --muted: #444444;
    --white: #ffffff;
  }
  * { box-sizing: border-box; margin: 0; padding: 0; }
  html, body { width: 1200px; height: 1200px; overflow: hidden; }
  body { background: var(--backdrop); position: relative; font-family: "Open Sans", sans-serif; }

  .card {
    position: absolute; left: 120px; width: 960px; height: 540px;
    background: var(--card); overflow: hidden;
    box-shadow: 0 6px 22px rgba(0,0,0,.18);
  }
  .card--front { top: 40px; }
  .card--back { top: 620px; }
  .card__shapes { position: absolute; inset: 0; width: 100%; height: 100%; }
  .card__shapes .green { fill: var(--green); }
  .card__shapes .pink { fill: var(--pink); }

  .web-tab {
    position: absolute; color: var(--white); font-weight: 600; letter-spacing: .3px; white-space: nowrap;
  }
  .card--front .web-tab { left: 34px; top: 52px; font-size: 19px; }
  .card--back .web-tab { left: 0; right: 0; bottom: 16px; text-align: center; font-size: 24px; }

  .holder { position: absolute; right: 46px; top: 38px; text-align: right; }
  .holder__name { font-family: "Poiret One", sans-serif; font-size: 38px; color: var(--ink); font-weight: 400; }
  .holder__role { font-family: "Open Sans", sans-serif; font-size: 12px; color: var(--muted); margin-top: 2px; }

  .brand { position: absolute; display: flex; align-items: center; }
  .brand__dot { border-radius: 50%; background: var(--pink); flex: none; }
  .brand__name { font-family: "Didact Gothic", sans-serif; color: var(--ink); white-space: nowrap; }
  .tagline {
    position: absolute; display: flex; align-items: center; white-space: nowrap;
    font-family: "Didact Gothic", sans-serif; color: var(--ink);
  }
  .tagline::before, .tagline::after { content: ""; height: 2px; background: var(--ink); flex: 1; }

  .card--front .brand { left: 90px; top: 190px; gap: 18px; }
  .card--front .brand__dot { width: 46px; height: 46px; }
  .card--front .brand__name { font-size: 66px; }
  .card--front .tagline { left: 90px; top: 284px; width: 520px; gap: 12px; font-size: 16px; }

  .card--back .brand { left: 0; right: 0; top: 170px; justify-content: center; gap: 26px; }
  .card--back .brand__dot { width: 66px; height: 66px; }
  .card--back .brand__name { font-size: 92px; }
  .card--back .tagline { left: 200px; top: 310px; width: 560px; gap: 14px; font-size: 21px; }

  .contacts { position: absolute; left: 58px; top: 380px; font-size: 18px; color: var(--ink); }
  .contacts__row { display: flex; gap: 36px; }
  .contacts__item { display: flex; align-items: center; gap: 8px; margin-bottom: 8px; }
  .contacts__item svg { width: 18px; height: 18px; flex: none; }
</style>
</head>
<body>

<section class="card card--front" aria-label="Business card front">
  <svg class="card__shapes" viewBox="0 0 960 540" aria-hidden="true">
    <rect class="pink" x="0" y="0" width="960" height="22"/>
    <path class="green" d="M0 0 H470 C420 6 420 100 352 104 H0 Z"/>
    <path class="pink" d="M0 450 H620 C680 450 720 438 760 424 L800 424 V540 H0 Z"/>
    <path class="green" d="M0 470 H630 C700 470 730 454 770 436 C830 410 800 300 870 268 C900 255 930 254 960 254 V540 H0 Z"/>
  </svg>

  <p class="web-tab">www.toffeeparlourco.example</p>

  <div class="holder">
    <p class="holder__name">Renata Hollis</p>
    <p class="holder__role">CEO &amp; Candy Stylist</p>
  </div>

  <div class="brand">
    <span class="brand__dot"></span>
    <span class="brand__name">toffee parlour</span>
  </div>
  <p class="tagline">sweet tables for every occasion</p>

  <div class="contacts">
    <div class="contacts__row">
      <p class="contacts__item">
        <svg viewBox="0 0 20 20" aria-hidden="true"><path fill="#ec1e86" d="M5 2 L8 2 L9 6 L7 8 C8 11 9 12 12 13 L14 11 L18 12 L18 15 C18 17 16 18 14 18 C8 17 3 12 2 6 C2 4 3 2 5 2 Z"/></svg>
        415.372.6091
      </p>
      <p class="contacts__item">
        <svg viewBox="0 0 20 20" aria-hidden="true"><rect x="1" y="4" width="18" height="12" fill="#ec1e86"/><path d="M1 4 L10 11 L19 4" fill="none" stroke="#fff" stroke-width="1.6"/></svg>
        renata@toffeeparlourco.example
      </p>
    </div>
    <p class="contacts__item">
      <svg viewBox="0 0 20 20" aria-hidden="true"><circle cx="10" cy="10" r="8.5" fill="none" stroke="#ec1e86" stroke-width="2"/><ellipse cx="10" cy="10" rx="3.5" ry="8.5" fill="none" stroke="#ec1e86" stroke-width="1.5"/><path d="M2 10 H18 M3.5 6 H16.5 M3.5 14 H16.5" stroke="#ec1e86" stroke-width="1.5"/></svg>
      www.toffeeparlourco.example
    </p>
  </div>
</section>

<section class="card card--back" aria-label="Business card back">
  <svg class="card__shapes" viewBox="0 0 960 540" aria-hidden="true">
    <rect class="pink" x="0" y="0" width="960" height="36"/>
    <path class="green" d="M0 470 H180 C230 470 250 540 280 540 H0 Z"/>
    <path class="pink" d="M262 540 C290 480 310 468 360 468 H780 C830 468 850 480 880 540 Z"/>
    <path class="green" d="M960 470 H930 C890 470 860 520 840 540 H960 Z"/>
  </svg>

  <div class="brand">
    <span class="brand__dot"></span>
    <span class="brand__name">toffee parlour</span>
  </div>
  <p class="tagline">sweet tables for every occasion</p>

  <p class="web-tab">www.toffeeparlourco.example</p>
</section>

</body>
</html>
```